Vantrelo App Homepage Design making customers feel in control of their spend

Hi,
We need a App Homepage design with a UI similar to the attached mock up on an Quorix 4. The app is intended to put customers in control of their usage and spend on their fixed phone, broadband, mobile, gas and electricity.

Please fee free to propose improvements to the background images, icons, colours, etc.

Any questions please let me know.

Thanks
Bertram

Target Market(s)

Consumer customers

Industry/Entity Type

Internet

Font styles to use
Sans Serif

Colors
3276b5
0255a3
85acd3
cfdeed
ffffff

Requirements
Must have
• Content in line with the guidelines in the attached mock up

```html
<!DOCTYPE html>
<html lang="en">
<head>
<meta charset="utf-8">
<title>Vantrelo App Home</title>
<link rel="stylesheet" href="https://fonts.googleapis.com/css2?family=Open+Sans:ital,wght@0,300;0,400;0,600;0,700;1,400&display=swap">
<style>
:root{
  --stage:#6fc6c8;
  --navy:#0a2f6b;
  --navy-deep:#08285c;
  --band:#41678f;
  --white:#ffffff;
  --brand:#0255a3;
  --soft-blue:#85acd3;
  --pink:#d3177f;
  --orange:#e5461a;
  --sky:#5a9fe6;
  --olive:#8ea81e;
  --flame:#e8531c;
  --bulb:#8a3d97;
  --ring:#0c2d5c;
}
*{margin:0;padding:0;box-sizing:border-box}
html,body{width:831px;height:1200px;overflow:hidden}
body{background:linear-gradient(160deg,#3f8c8e 0%,var(--stage) 55%,#9eeaef 100%);font-family:"Open Sans",sans-serif;color:var(--white)}
.screen{position:absolute;left:84px;top:11px;width:662px;height:1177px;background:var(--navy);overflow:hidden}
.screen-bg{position:absolute;inset:0}
.status-bar{position:absolute;left:0;top:0;width:100%;height:48px;display:flex;align-items:center;justify-content:space-between;padding:0 16px;font-size:20px;font-weight:400}
.status-time{position:absolute;left:50%;transform:translateX(-50%);font-weight:600}
.app-header{position:absolute;top:88px;left:0;width:100%;height:66px}
.menu-icon{position:absolute;left:28px;top:17px}
.brand{position:absolute;left:50%;top:0;transform:translateX(-50%);display:flex;align-items:center;gap:14px;height:66px}
.brand-dot{width:44px;height:44px;border-radius:50%;background:var(--brand)}
.brand-name{font-size:46px;font-weight:600;color:var(--brand);letter-spacing:-0.5px}
.settings-icon{position:absolute;right:22px;top:10px}
.avatar{position:absolute;left:156px;top:217px;width:146px;height:146px;border-radius:50%;border:5px solid #1b6b63;background:radial-gradient(circle at 45% 40%,#e9d3c2,#a88f80 60%,#6e6a68)}
.greeting{position:absolute;left:0;width:338px;text-align:center}
.greeting-title{top:383px;font-size:27px;font-weight:700}
.greeting-sub{top:426px;font-size:23px;font-style:italic;color:var(--soft-blue)}
.service{position:absolute;width:106px;height:106px;border-radius:50%;background:var(--white);display:flex;align-items:center;justify-content:center;box-shadow:0 4px 10px rgba(0,0,0,.25)}
.charges{position:absolute;left:348px;top:696px;width:294px;height:294px}
.charges-label{position:absolute;left:0;top:94px;width:100%;text-align:center;font-size:25px;font-weight:300;line-height:40px}
.charges-amount{display:block;font-size:40px;font-weight:700;line-height:50px}
.bill{position:absolute;left:20px}
.bill-latest{top:1000px;font-size:43px;font-weight:300}
.bill-latest b{font-weight:700}
.bill-date{top:1066px;font-size:36px;font-weight:300}
.bill-renew{top:1113px;font-size:21px;font-weight:400}
</style>
</head>
<body>
<main class="screen">
  <svg class="screen-bg" width="662" height="1177" viewBox="0 0 662 1177" aria-hidden="true">
    <rect width="662" height="1177" fill="var(--navy)"/>
    <polygon points="0,0 662,0 0,909" fill="var(--band)"/>
  </svg>

  <div class="status-bar">
    <span class="status-carrier">●●●○○ VANTRELO</span>
    <span class="status-time">4:21 PM</span>
    <span class="status-battery">100% ▬</span>
  </div>

  <header class="app-header">
    <svg class="menu-icon" width="40" height="32" viewBox="0 0 40 32" aria-label="Menu">
      <rect y="0" width="40" height="4" rx="2" fill="#fff"/>
      <rect y="14" width="40" height="4" rx="2" fill="#fff"/>
      <rect y="28" width="40" height="4" rx="2" fill="#fff"/>
    </svg>
    <div class="brand"><span class="brand-dot"></span><span class="brand-name">Vantrelo</span></div>
    <svg class="settings-icon" width="46" height="46" viewBox="0 0 46 46" aria-label="Settings">
      <g fill="#fff" transform="translate(23 23)">
        <rect x="-5" y="-22" width="10" height="44" rx="2"/>
        <rect x="-5" y="-22" width="10" height="44" rx="2" transform="rotate(45)"/>
        <rect x="-5" y="-22" width="10" height="44" rx="2" transform="rotate(90)"/>
        <rect x="-5" y="-22" width="10" height="44" rx="2" transform="rotate(135)"/>
        <circle r="16"/>
      </g>
      <circle cx="23" cy="23" r="7" fill="var(--band)"/>
    </svg>
  </header>

  <div class="avatar" role="img" aria-label="Profile photo of the customer"></div>
  <p class="greeting greeting-title">Good morning Marla</p>
  <p class="greeting greeting-sub">Welcome to Vantrelo</p>

  <div class="service" style="left:519px;top:215px" aria-label="Fixed phone">
    <svg width="54" height="54" viewBox="0 0 24 24"><path fill="var(--navy)" d="M6.6 10.8a15.1 15.1 0 0 0 6.6 6.6l2.2-2.2c.3-.3.7-.4 1-.2 1.1.4 2.3.6 3.6.6.6 0 1 .4 1 1V20c0 .6-.4 1-1 1A17 17 0 0 1 3 4c0-.6.4-1 1-1h3.5c.6 0 1 .4 1 1 0 1.3.2 2.5.6 3.6.1.3 0 .7-.2 1z"/></svg>
  </div>
  <div class="service" style="left:416px;top:363px" aria-label="Broadband">
    <svg width="56" height="50" viewBox="0 0 56 50" fill="none" stroke="var(--sky)" stroke-width="6" stroke-linecap="round">
      <path d="M4 18a34 34 0 0 1 48 0"/><path d="M13 27a21 21 0 0 1 30 0"/><path d="M21 36a9 9 0 0 1 14 0"/>
      <circle cx="28" cy="44" r="3" fill="var(--sky)" stroke="none"/>
    </svg>
  </div>
  <div class="service" style="left:312px;top:510px" aria-label="Gas">
    <svg width="44" height="60" viewBox="0 0 44 60"><path fill="var(--flame)" d="M24 2c2 12 18 20 18 36a20 20 0 0 1-40 0c0-10 6-14 8-22 4 6 4 10 2 16 6-4 10-14 12-30z"/><path fill="#fff" d="M22 34c4 6 8 9 8 15a8 8 0 0 1-16 0c0-5 4-8 8-15z"/></svg>
  </div>
  <div class="service" style="left:209px;top:657px" aria-label="Mobile">
    <svg width="30" height="54" viewBox="0 0 30 54"><rect x="2" y="2" width="26" height="50" rx="5" fill="none" stroke="var(--navy)" stroke-width="4"/><rect x="6" y="9" width="18" height="32" fill="var(--navy)"/><circle cx="15" cy="46" r="2.5" fill="var(--navy)"/></svg>
  </div>
  <div class="service" style="left:105px;top:805px" aria-label="Electricity">
    <svg width="56" height="60" viewBox="0 0 56 60" fill="none" stroke="var(--bulb)" stroke-width="3.5" stroke-linecap="round">
      <path d="M20 42c0-6-8-9-8-19a16 16 0 0 1 32 0c0 10-8 13-8 19z"/>
      <path d="M21 48h14M23 54h10"/>
      <path d="M4 10l5 4M52 10l-5 4M28 1v2"/>
    </svg>
  </div>

  <div class="charges">
    <svg width="294" height="294" viewBox="0 0 294 294" aria-hidden="true">
      <circle cx="147" cy="147" r="145" fill="var(--ring)"/>
      <circle cx="147" cy="147" r="133" fill="var(--navy-deep)"/>
      <g fill="none" stroke-width="46" transform="rotate(-90 147 147)">
        <circle cx="147" cy="147" r="108" stroke="var(--pink)" stroke-dasharray="170 509"/>
        <circle cx="147" cy="147" r="108" stroke="var(--orange)" stroke-dasharray="292 387" stroke-dashoffset="-170"/>
        <circle cx="147" cy="147" r="108" stroke="var(--sky)" stroke-dasharray="94 585" stroke-dashoffset="-462"/>
        <circle cx="147" cy="147" r="108" stroke="var(--olive)" stroke-dasharray="85 594" stroke-dashoffset="-556"/>
        <circle cx="147" cy="147" r="108" stroke="#0d3474" stroke-dasharray="38 641" stroke-dashoffset="-641"/>
      </g>
      <circle cx="147" cy="147" r="85" fill="var(--navy-deep)"/>
    </svg>
    <p class="charges-label">Your Current<br>Charges<span class="charges-amount">£63.99</span></p>
  </div>

  <p class="bill bill-latest">Latest bill : <b>£72.90</b></p>
  <p class="bill bill-date">9 Dec 2016</p>
  <p class="bill bill-renew">Allowance renews in 18 days</p>
</main>
</body>
</html>
```